Design layout of business card

Create a business card using existing logo and company information.
Our newly established business provides advice to family owned businesses for their succession planning, value improvement and also on business sales and acquisitions.

Target Market(s)

Owners of family businesses

Contact Information for Business Card

Key contact details are:
Grant Mellowby
Director
P: 08 9482 3157
W: 0431 587 219
Address: Unit 4, 35 Talbrook Lane, Carrowbay, WA, 6297
Website: kinholdadvisory.com.au
Email: grant@kinholdadvisory.com.au

In smaller font somewhere needs to be these details:
ABN: 47 291 803 556
Licensed Real Estate & Business Agent No. RA53917
KTR Adviser Holdings Pty Ltd
AFSL No. 529361

Font styles to use
Sans Serif

Requirements
Must have
• Kinhold Advisory Group logo to feature on front.
• Remaining logos to be included smaller and on back.
• Oakvale Trade Brokers logo to have words 'Powered by' next to it and to be the first of the uploaded logo files.
• Colours on card should complement the logo
Nice to have
• Clear and clean layout
• Logos for contact details for conciseness e.g. phone icon for mobile

```html
<!DOCTYPE html>
<html lang="en">
<head>
<meta charset="utf-8">
<title>Kinhold Advisory Group – Business Card</title>
<link rel="stylesheet" href="https://fonts.googleapis.com/css2?family=Montserrat:wght@600&family=Roboto:wght@400;700&display=swap">
<style>
:root{
  --brand-orange:#e44f21;
  --brand-grey:#7d8589;
  --ink:#3f4245;
  --paper:#ffffff;
  --strip:#ececec;
  --backdrop:#e9e7e3;
  --partner-blue:#2f4d8f;
  --partner-gold:#d9a93a;
  --partner-navy:#1f3057;
}
*{margin:0;padding:0;box-sizing:border-box}
html,body{width:1200px;height:959px;overflow:hidden;background:var(--backdrop)}
.sheet{position:relative;width:1200px;height:959px}
.card{position:absolute;left:240px;width:720px;height:430px;background:var(--paper);overflow:hidden;box-shadow:0 4px 14px rgba(0,0,0,.12)}
.card--front{top:30px}
.card--back{top:499px}

/* front */
.front-band{position:absolute;left:0;top:0;width:720px;height:330px;background:var(--brand-orange);display:flex;align-items:center;justify-content:center;gap:26px}
.brand-mark{width:108px;height:108px;border-radius:50%;border:7px solid var(--paper);flex:none}
.brand-name{font-family:"Montserrat",sans-serif;font-weight:600;font-size:44px;line-height:1.02;color:var(--paper)}
.front-strip{position:absolute;left:0;top:330px;width:720px;height:100px;background:var(--strip);display:flex;align-items:center;justify-content:center;gap:18px}
.powered-by{font-family:"Roboto",sans-serif;font-size:18px;color:var(--ink)}
.partner-badge{width:40px;height:40px;border-radius:50%;background:var(--partner-blue);border:3px solid var(--partner-gold);flex:none}
.partner-name{font-family:"Roboto",sans-serif;font-weight:700;font-size:11px;letter-spacing:.08em;color:var(--partner-navy);text-transform:uppercase}
.partner-name--light{font-weight:400;font-size:9px;color:var(--ink)}

/* back */
.back-brand{position:absolute;left:56px;top:120px;display:flex;align-items:center;gap:16px}
.back-brand .brand-mark{width:86px;height:86px;border:5px solid var(--brand-grey)}
.back-brand .brand-name{font-size:30px;color:var(--brand-orange)}
.divider{position:absolute;left:356px;top:52px;width:2px;height:200px;background:var(--brand-grey)}
.contact{position:absolute;left:380px;top:48px;font-family:"Roboto",sans-serif;color:var(--ink);font-size:16px;line-height:1.35}
.contact__name{font-family:"Montserrat",sans-serif;font-weight:600;font-size:23px;color:var(--brand-orange);line-height:1.1}
.contact__role{font-weight:700;font-size:16px;margin-bottom:6px}
.contact__line{display:flex;align-items:center;gap:8px}
.contact__line svg{width:15px;height:15px;flex:none}
.legal{position:absolute;left:0;right:0;top:300px;text-align:center;font-family:"Roboto",sans-serif;font-size:15px;line-height:1.4;color:var(--ink)}
</style>
</head>
<body>
<main class="sheet">

  <section class="card card--front" aria-label="Card front">
    <div class="front-band">
      <span class="brand-mark"></span>
      <span class="brand-name">Kinhold<br>Advisory<br>Group</span>
    </div>
    <div class="front-strip">
      <span class="powered-by">Powered by</span>
      <span class="partner-badge" role="img" aria-label="Oakvale Trade Brokers badge"></span>
      <span class="partner-name">Westline Brokers Institute</span>
      <span class="partner-badge" role="img" aria-label="Member badge"></span>
      <span class="partner-name partner-name--light">oakvalegroup.com.au</span>
    </div>
  </section>

  <section class="card card--back" aria-label="Card back">
    <div class="back-brand">
      <span class="brand-mark"></span>
      <span class="brand-name">Kinhold<br>Advisory<br>Group</span>
    </div>
    <div class="divider"></div>
    <div class="contact">
      <div class="contact__name">Grant Mellowby</div>
      <div class="contact__role">Director</div>
      <div>Unit 4, 35 Talbrook Lane,</div>
      <div>Carrowbay, WA, 6297</div>
      <div class="contact__line">
        <svg viewBox="0 0 16 16"><path fill="var(--brand-orange)" d="M3 1l3 3-1.5 2a9 9 0 0 0 5.5 5.5L12 10l3 3-2 2C7 15 1 9 1 3z"/></svg>
        08 9482 3157
      </div>
      <div class="contact__line">
        <svg viewBox="0 0 16 16"><rect x="4" y="1" width="8" height="14" rx="1.5" fill="var(--brand-orange)"/><rect x="5.5" y="3" width="5" height="8" fill="#fff"/></svg>
        0431 587 219
      </div>
      <div class="contact__line">
        <svg viewBox="0 0 16 16"><rect x="1" y="3" width="14" height="10" rx="1" fill="var(--brand-orange)"/><path d="M1.5 3.5L8 9l6.5-5.5" stroke="#fff" stroke-width="1.3" fill="none"/></svg>
        grant@kinholdadvisory.com.au
      </div>
      <div class="contact__line">
        <svg viewBox="0 0 16 16"><circle cx="8" cy="8" r="7" fill="var(--brand-orange)"/><path d="M1 8h14M8 1c-3 3-3 11 0 14M8 1c3 3 3 11 0 14" stroke="#fff" stroke-width="1" fill="none"/></svg>
        www.kinholdadvisory.com.au
      </div>
    </div>
    <div class="legal">
      KTR Adviser Holdings Pty Ltd<br>
      ABN: 47 291 803 556 AFSL No. 529361<br>
      Licensed Real Estate &amp; Business Agent No. RA53917
    </div>
  </section>

</main>
</body>
</html>
```